Copperfield interiors PTY LTD

My business specializes in commercial fitout which builds walls, ceilings, doors, uses also materials aluminium in works. Id like to have a logo designed for my company too.

Industry/Entity Type

Business

```html
<!DOCTYPE html>
<html lang="en">
<head>
<meta charset="utf-8">
<title>Copperfield Interiors – Business Card</title>
<link rel="stylesheet" href="https://fonts.googleapis.com/css2?family=Montserrat:wght@700&family=Open+Sans:wght@400;700&display=swap">
<style>
  :root {
    --backdrop: #e4e4e4;
    --blue-light: #0a8fdc;
    --blue-dark: #0d63b0;
    --white: #ffffff;
    --paper: #f5f6f7;
    --divider: #3c4148;
    --brand-blue: #1768b4;
  }
  * { box-sizing: border-box; margin: 0; padding: 0; }
  html, body {
    width: 1200px; height: 852px; overflow: hidden;
    background: var(--backdrop);
  }
  .stage {
    position: relative; width: 1200px; height: 852px;
  }
  .card {
    position: absolute; width: 520px; height: 300px;
    border-radius: 26px; overflow: hidden;
    background: linear-gradient(160deg, var(--blue-light) 0%, var(--blue-dark) 100%);
  }
  .card--front { left: 60px; top: 90px; }
  .card--back { left: 620px; top: 462px; }

  .front-brand {
    position: absolute; inset: 0;
    display: flex; flex-direction: column; align-items: center; justify-content: center;
    color: var(--white); font-family: "Montserrat", sans-serif; font-weight: 700;
  }
  .front-brand .name { font-size: 40px; letter-spacing: 1px; line-height: 1; }
  .front-brand .sub { font-size: 15px; letter-spacing: 11px; margin-top: 6px; padding-left: 11px; }

  .back-panel { position: absolute; inset: 0; }
  .back-brand {
    position: absolute; left: 22px; top: 118px; width: 170px;
    color: var(--brand-blue); font-family: "Montserrat", sans-serif; font-weight: 700;
  }
  .back-brand .name { font-size: 22px; line-height: 1; }
  .back-brand .sub { font-size: 11px; letter-spacing: 6px; margin-top: 6px; }

  .contact {
    position: absolute; left: 268px; top: 54px;
    color: var(--white); font-family: "Open Sans", sans-serif;
  }
  .contact .person { font-size: 22px; font-weight: 700; line-height: 1.1; }
  .contact .role { font-size: 12px; margin-top: 4px; }
  .contact .lines { list-style: none; margin-top: 22px; font-size: 13px; line-height: 1.45; }
  .contact .lines li { display: flex; align-items: center; gap: 10px; white-space: nowrap; }
  .contact .lines svg { width: 12px; height: 12px; flex: none; }
  .contact .lines .plain { padding-left: 22px; }
</style>
</head>
<body>
<main class="stage">
  <section class="card card--front">
    <div class="front-brand">
      <span class="name">COPPERFIELD</span>
      <span class="sub">INTERIORS</span>
    </div>
  </section>

  <section class="card card--back">
    <svg class="back-panel" viewBox="0 0 520 300" preserveAspectRatio="none">
      <path d="M0 0 H170 C215 80 225 190 218 300 H0 Z" fill="var(--paper)"/>
      <path d="M170 0 C215 80 225 190 218 300" fill="none" stroke="var(--divider)" stroke-width="7"/>
    </svg>
    <div class="back-brand">
      <div class="name">COPPERFIELD</div>
      <div class="sub">INTERIORS</div>
    </div>
    <div class="contact">
      <div class="person">Alex Morgan Reed</div>
      <div class="role">Managing Director</div>
      <ul class="lines">
        <li><svg viewBox="0 0 12 12"><path d="M2 1h2.5l1 3-1.5 1a7 7 0 0 0 3 3l1-1.5 3 1V10a1 1 0 0 1-1 1A9 9 0 0 1 1 2a1 1 0 0 1 1-1z" fill="var(--white)"/></svg>555.210.4836</li>
        <li><svg viewBox="0 0 12 12"><rect x="0.5" y="2" width="11" height="8" fill="var(--white)"/><path d="M0.5 2 6 6.5 11.5 2" fill="none" stroke="var(--blue-dark)" stroke-width="1"/></svg>alex@copperfieldfitout.com</li>
        <li><svg viewBox="0 0 12 12"><circle cx="6" cy="6" r="5.2" fill="none" stroke="var(--white)" stroke-width="1.2"/><ellipse cx="6" cy="6" rx="2.2" ry="5.2" fill="none" stroke="var(--white)" stroke-width="1"/><path d="M1 6h10" stroke="var(--white)" stroke-width="1"/></svg>www.copperfieldfitout.com</li>
        <li class="plain">18 Harbour Lane,</li>
        <li class="plain">Riverton, US 204815</li>
      </ul>
    </div>
  </section>
</main>
</body>
</html>
```